Business Card Ayurvedic Massage

I'm starting with my ayurvedic massage business and need a business card design. The design should be inline with my brand/logo as well as with the design of my website (www.mirelo-dant.ch).
Front: logo and text "Ayurvedische Massagen"
back: name and adress (see details https://www.mirelo-dant.ch/kontakt.html)

```html
<!DOCTYPE html>
<html lang="de">
<head>
<meta charset="utf-8">
<title>Mirelo-Dant – Visitenkarte</title>
<link href="https://fonts.googleapis.com/css2?family=Open+Sans+Condensed:wght@500;700&family=Open+Sans:wght@400;600&display=swap" rel="stylesheet">
<style>
  :root {
    --backdrop: #8c8c8c;
    --card-red: #7a1419;
    --card-red-dark: #5e0d12;
    --gold: #d9a441;
    --band-red: #d2261a;
    --band-orange: #f08a12;
    --band-yellow: #ffe21a;
    --ink: #1a0a08;
    --line: rgba(0,0,0,0.22);
  }
  * { margin: 0; padding: 0; box-sizing: border-box; }
  html, body { width: 1200px; height: 800px; overflow: hidden; }
  body {
    background: var(--backdrop);
    font-family: "Open Sans Condensed", "Open Sans", sans-serif;
    display: flex; align-items: center; justify-content: center; gap: 70px;
  }
  .card {
    position: relative;
    background: radial-gradient(ellipse at 40% 30%, var(--card-red), var(--card-red-dark));
    box-shadow: 0 10px 30px rgba(0,0,0,0.3);
    overflow: hidden;
  }
  .band {
    position: absolute;
    display: flex; align-items: center;
    color: var(--ink); font-weight: 700; text-transform: uppercase; letter-spacing: 0.5px;
  }
  /* Front */
  .card--front { width: 560px; height: 364px; }
  .card--front .band {
    left: 0; right: 0; bottom: 30px; height: 26px;
    background: linear-gradient(to bottom, var(--band-red), var(--band-orange) 30%, var(--band-yellow) 50%, var(--band-orange) 70%, var(--band-red));
    justify-content: flex-end; padding-right: 28px; font-size: 13px;
  }
  .brand { position: absolute; left: 40px; top: 150px; width: 240px; }
  .brand__mark { display: flex; align-items: center; gap: 10px; }
  .brand__dot { width: 14px; height: 14px; border-radius: 50%; background: var(--gold); }
  .brand__name { color: var(--gold); font-size: 30px; font-weight: 700; }
  .brand__art { display: block; width: 220px; height: 40px; margin-top: 10px; }
  .brand__tagline { color: var(--gold); font-size: 15px; font-weight: 500; text-transform: uppercase; margin-top: 8px; letter-spacing: 0.5px; }
  .contact {
    position: absolute; left: 300px; top: 40px; right: 0; height: 240px;
    border-left: 1px solid var(--line); border-bottom: 1px solid var(--line);
    padding: 50px 20px 0 30px; list-style: none;
    color: var(--gold); font-size: 13px; line-height: 1.35; text-transform: uppercase;
  }
  .contact li { display: flex; align-items: flex-start; gap: 12px; margin-bottom: 10px; }
  .contact svg { flex: none; width: 20px; height: 20px; }
  /* Back */
  .card--back { width: 364px; height: 560px; }
  .card--back .band {
    top: 0; bottom: 0; left: 26px; width: 26px;
    background: linear-gradient(to right, var(--band-red), var(--band-orange) 30%, var(--band-yellow) 50%, var(--band-orange) 70%, var(--band-red));
    justify-content: center; font-size: 13px;
  }
  .band__text { writing-mode: vertical-rl; transform: rotate(180deg); margin-top: 220px; }
  .back-brand { position: absolute; left: 90px; top: 70px; width: 240px; }
  .menu {
    position: absolute; left: 170px; top: 300px; right: 0; bottom: 0;
    border-left: 1px solid var(--line); border-top: 1px solid var(--line);
    padding: 26px 16px; list-style: none; color: var(--ink);
    font-size: 20px; font-weight: 700; text-transform: uppercase; line-height: 1.15;
  }
  .menu li { display: flex; align-items: center; gap: 8px; }
  .menu svg { width: 14px; height: 14px; flex: none; }
  .menu__url { color: var(--gold); font-size: 12px; font-weight: 500; margin-top: 14px; }
</style>
</head>
<body>
  <section class="card card--front" aria-label="Vorderseite">
    <div class="brand">
      <div class="brand__mark"><span class="brand__dot"></span><span class="brand__name">mirelo-dant</span></div>
      <svg class="brand__art" role="img" aria-label="Dekorative Elefantenillustration in Gold"><rect width="220" height="40" rx="4" fill="#b07a2e" opacity="0.55"/></svg>
      <p class="brand__tagline">Ayurvedische Massagen</p>
    </div>
    <ul class="contact">
      <li><svg viewBox="0 0 20 20"><circle cx="10" cy="10" r="9" fill="var(--gold)"/><path d="M7 5l2 2-1 1.5c.7 1.5 1.8 2.6 3.3 3.3L12.8 11l2 2-1.5 1.5C9.5 14 6 10.5 5.5 6.7z" fill="var(--ink)"/></svg><span>+41 77 000 12 34</span></li>
      <li><svg viewBox="0 0 20 20"><circle cx="10" cy="10" r="9" fill="var(--gold)"/><circle cx="10" cy="10" r="3.2" fill="none" stroke="var(--ink)" stroke-width="1.5"/><path d="M13.2 10v1.3a1.5 1.5 0 003 0V10a6.2 6.2 0 10-2.4 4.9" fill="none" stroke="var(--ink)" stroke-width="1.5"/></svg><span>info@mirelo-dant.ch</span></li>
      <li><svg viewBox="0 0 20 20"><circle cx="10" cy="10" r="9" fill="var(--gold)"/><path d="M5 10l5-4.5 5 4.5M6.5 9v5h7V9" fill="none" stroke="var(--ink)" stroke-width="1.5"/></svg><span>Lina Varenholt, Mirelo-Dant,<br>Brunnmattweg 14,<br>8861 Felsbach (SZ)</span></li>
    </ul>
    <div class="band">http://www.mirelo-dant.ch</div>
  </section>

  <section class="card card--back" aria-label="Rückseite">
    <div class="band"><span class="band__text">Ayurvedische Massagen</span></div>
    <div class="back-brand">
      <div class="brand__mark"><span class="brand__dot"></span><span class="brand__name">mirelo-dant</span></div>
      <svg class="brand__art" role="img" aria-label="Dekorative Elefantenillustration in Gold"><rect width="220" height="40" rx="4" fill="#b07a2e" opacity="0.55"/></svg>
    </div>
    <ul class="menu">
      <li><svg viewBox="0 0 14 14"><circle cx="7" cy="7" r="6" fill="var(--band-yellow)"/></svg>Ayurveda</li>
      <li><svg viewBox="0 0 14 14"><circle cx="7" cy="7" r="6" fill="var(--band-yellow)"/></svg>Behandlungen</li>
      <li><svg viewBox="0 0 14 14"><circle cx="7" cy="7" r="6" fill="var(--band-yellow)"/></svg>Preise</li>
      <li><svg viewBox="0 0 14 14"><circle cx="7" cy="7" r="6" fill="var(--band-yellow)"/></svg>Praxis</li>
      <li class="menu__url">http://www.mirelo-dant.ch</li>
    </ul>
  </section>
</body>
</html>
```